Managed IT services business card design

We haven't needed a business card since the founding of the business in 2005. All our clients have been coming through word of mouth. And lately more and more existing clients are requesting for our business cards to pass on to their contacts in recommending us.
So we needing a business card design. We use various innovative solutions and methodologies to provide IT services to small businesses in managing their IT systems. Our role is the same as an in-house, full-time IT Manager for our clients, but outsourced. So we take care of all our clients' IT needs, just as an IT Manager would be expected to perform.
We have a holding website, which we're happy to leave for now. If we can use the same logo would be great - www.lomvex.com.au
Preferred colours are shades of are white, grey and black.
We pride our business with the following traits: proactive, good service, prompt response, trustworthy.
Target Market(s)
Small businesses of any industry
Industry/Entity Type
Business

```html
<!DOCTYPE html>
<html lang="en">
<head>
<meta charset="utf-8">
<title>Lomvex Business Card</title>
<link href="https://fonts.googleapis.com/css2?family=Open+Sans:wght@300;400;600&display=swap" rel="stylesheet">
<style>
  :root {
    --page-bg: #e4e4e4;
    --card-centre: #5a5a5a;
    --card-edge: #1e1e1e;
    --text-light: #f2f2f2;
    --text-soft: #d6d6d6;
    --rule-light: #9a9a9a;
    --rule-dark: #0e0e0e;
    --icon-bg: #efefef;
    --icon-ink: #2a2a2a;
  }
  html, body {
    margin: 0;
    width: 1200px;
    height: 1000px;
    overflow: hidden;
    background: var(--page-bg);
    font-family: "Open Sans", Arial, sans-serif;
  }
  .business-card {
    position: absolute;
    left: 165px;
    top: 250px;
    width: 870px;
    height: 500px;
    background: radial-gradient(ellipse at 60% 30%, var(--card-centre) 0%, #3c3c3c 45%, var(--card-edge) 100%);
    box-shadow: 0 12px 30px rgba(0,0,0,0.35);
    overflow: hidden;
  }
  .edge-rules {
    position: absolute;
    top: 0;
    left: 52px;
    height: 100%;
    width: 20px;
  }
  .edge-rules span {
    position: absolute;
    top: 0;
    bottom: 0;
    width: 4px;
    background: var(--rule-light);
    box-shadow: 2px 0 0 var(--rule-dark);
  }
  .edge-rules span:first-child { left: 0; }
  .edge-rules span:last-child { left: 12px; }
  .brand-name {
    position: absolute;
    left: 100px;
    top: 48px;
    margin: 0;
    font-weight: 300;
    font-size: 52px;
    letter-spacing: 14px;
    color: var(--text-light);
    line-height: 1;
  }
  .person {
    position: absolute;
    left: 610px;
    top: 58px;
  }
  .person-name {
    margin: 0;
    font-weight: 600;
    font-size: 36px;
    color: var(--text-light);
    line-height: 1.1;
  }
  .person-role {
    margin: 2px 0 0;
    font-size: 27px;
    color: var(--text-soft);
    line-height: 1.1;
  }
  .contact-list {
    position: absolute;
    left: 100px;
    top: 306px;
    margin: 0;
    padding: 0;
    list-style: none;
    font-size: 21px;
    color: var(--text-soft);
  }
  .contact-list li {
    display: flex;
    align-items: center;
    height: 40px;
  }
  .contact-list li.address { height: 36px; }
  .contact-icon {
    width: 24px;
    height: 24px;
    margin-right: 28px;
    flex: none;
  }
</style>
</head>
<body>
  <div class="business-card">
    <div class="edge-rules"><span></span><span></span></div>

    <p class="brand-name">lomvex</p>

    <div class="person">
      <p class="person-name">Name Title</p>
      <p class="person-role">designation</p>
    </div>

    <ul class="contact-list">
      <li class="address">Hollis Lane, Melbourne</li>
      <li>
        <svg class="contact-icon" viewBox="0 0 24 24" aria-hidden="true">
          <rect width="24" height="24" rx="3" fill="var(--icon-bg)"/>
          <path d="M7 5 L10 5 L11 9 L9 10.5 Q10.5 13.5 13.5 15 L15 13 L19 14 L19 17 Q18 19 15.5 18.5 Q8 16 5.5 8.5 Q5 6 7 5 Z" fill="var(--icon-ink)"/>
        </svg>
        +61 412 555 018
      </li>
      <li>
        <svg class="contact-icon" viewBox="0 0 24 24" aria-hidden="true">
          <rect width="24" height="24" rx="3" fill="var(--icon-bg)"/>
          <path d="M4 9 L12 4 L20 9 L20 19 L4 19 Z" fill="var(--icon-ink)"/>
          <path d="M4 9 L12 14 L20 9" fill="none" stroke="var(--icon-bg)" stroke-width="1.6"/>
        </svg>
        mail@lomvex.com.au
      </li>
      <li>
        <svg class="contact-icon" viewBox="0 0 24 24" aria-hidden="true">
          <circle cx="12" cy="12" r="11" fill="var(--icon-bg)"/>
          <g fill="none" stroke="var(--icon-ink)" stroke-width="1.5">
            <circle cx="12" cy="12" r="8"/>
            <ellipse cx="12" cy="12" rx="3.5" ry="8"/>
            <line x1="4" y1="12" x2="20" y2="12"/>
            <line x1="5.5" y1="8" x2="18.5" y2="8"/>
            <line x1="5.5" y1="16" x2="18.5" y2="16"/>
          </g>
        </svg>
        www.lomvex.com.au
      </li>
    </ul>
  </div>
</body>
</html>
```